Photobook template design

Just one book of 4/5 pages needed to find a handful of designers to help with this project that will be ongoing for several months, we will agree design price per book.

Hi there, we need lots of fabulous photobook templates designed:
there will be 20 books to start with, canvas layouts, calendar layouts etc.

The MAIN idea of the template is to facilitate the easiest creation / ordering of photobooks etc. possible for the client, so all they have to do is upload their pics and drop them into the templates you're going to design...

Each photobook needs to have min 20 pages, there can be a common theme throughout, but they must be different enough so that they do not all blend into one.
Choose to create a design from the following categories:
family
kids
travel
romance / love
seasonal holiday
year in review
everyday / general
recipes
pets / animals
collage
scrapbook

the quality and look and feel must be equal to www.pagelark.com / www.snapvellum.com / www.printorra.co.uk

In order to keep the designs as fresh as possible - we will work with several designers, so for this first project we will choose 1 designer, but then we'll create other design projects for which you will be specifically invited to design for - it's the only way the do multiple designs/projects.

please see 2 pics attached of other templates already designed - we're very happy with these...

Target Market(s)

These photobooks / calendars / canvas prints are for the average family - not too serious, must be fun / tongue in cheek etc.
They're for people who want to do photobooks but have no clue or do not have the time - so they must LOVE the design, and then want to just add their photos...

Industry/Entity Type

Travel

Requirements
Must have
• Must be designed in Layoutra or Vectorix.
Metric sizes please - Either A3 landscape or portrait with 3 mm bleed, or 300 x 300mm square - 3mm bleed
If you place photos for proofing, please use imagewell images - we have a imagewell account

```html
<!DOCTYPE html>
<html lang="en">
<head>
<meta charset="utf-8">
<title>Moments With You – Photobook Template</title>
<link href="https://fonts.googleapis.com/css2?family=Quicksand:wght@300;400&family=Josefin+Sans:wght@300;400&family=Open+Sans:wght@400&display=swap" rel="stylesheet">
<style>
  :root {
    --backdrop: #e9e6e2;
    --cover-sage: #c5d6cc;
    --frame-white: #ffffff;
    --frame-line: #a3b9ae;
    --title-grey: #7a7a7a;
    --coral: #f28b7b;
    --page-white: #ffffff;
    --page-fade: #f1f1f1;
    --stripe-orange: #f3c89a;
    --stripe-teal: #b9d3cc;
    --body-grey: #8a8a8a;
    --ribbon-green: #7da776;
    --ribbon-gold: #c49416;
    --ribbon-plum: #a24a9e;
    --ribbon-lavender: #9a86c8;
    --border-magenta: #c9479e;
    --border-orchid: #b44aa6;
    --border-violet: #8a6bb5;
    --border-pink: #e46aa2;
    --border-orange: #ee7d2b;
    --fold: #d5d5d5;
  }
  * { box-sizing: border-box; margin: 0; padding: 0; }
  html, body {
    width: 1164px; height: 1200px; overflow: hidden;
    background: var(--backdrop);
  }
  .canvas { position: relative; width: 1164px; height: 1200px; }

  .spread {
    position: absolute; left: 37px; width: 1090px; height: 547px;
    box-shadow: 0 2px 6px rgba(0,0,0,0.18);
  }
  .spread--cover { top: 38px; background: var(--cover-sage); }
  .spread--inner {
    top: 618px;
    background: linear-gradient(180deg, var(--page-white) 0%, var(--page-white) 35%, var(--page-fade) 100%);
  }
  .spread__fold {
    position: absolute; left: 545px; top: 0; width: 1px; height: 100%;
    background: var(--fold);
  }
  .spread--cover .spread__fold { background: #b3c6bb; }

  /* Cover */
  .cover-ribbon {
    position: absolute; left: 0; top: 436px; width: 225px; height: 44px;
    background: var(--coral);
    clip-path: polygon(0 0, 100% 0, 94% 50%, 100% 100%, 0 100%);
    color: #fff; font-family: "Quicksand", sans-serif; font-weight: 300;
    font-size: 14px; line-height: 44px; padding-left: 48px;
  }
  .cover-frame { position: absolute; left: 603px; top: 54px; width: 432px; height: 437px; }
  .cover-frame svg { position: absolute; inset: 0; }
  .cover-photo {
    position: absolute; left: 52px; top: 38px; width: 326px; height: 326px;
    background: radial-gradient(circle at 40% 55%, #d9b49a 0%, #a57d62 30%, #6d8c3c 65%, #9cc04a 100%);
  }
  .cover-title {
    position: absolute; left: 0; top: 380px; width: 432px; text-align: center;
    font-family: "Quicksand", sans-serif; font-weight: 300; font-size: 30px;
    color: var(--title-grey); letter-spacing: 0.3px;
  }

  /* Inner pages */
  .stripe-band { position: absolute; left: 0; width: 100%; }
  .stripe-band__line { height: 0; border-top: 1px dotted var(--stripe-orange); margin-bottom: 5px; }
  .stripe-band__rule { height: 0; border-top: 1px solid var(--stripe-teal); }
  .stripe-band--top { top: 10px; }
  .stripe-band--bottom { top: 496px; }

  .photo {
    position: absolute; border: 2px solid;
  }
  .photo--her-portrait { left: 34px; top: 74px; width: 147px; height: 97px; border-color: var(--border-magenta);
    background: linear-gradient(135deg, #7fae4a 0%, #a9c46b 45%, #c7a083 70%, #6f9a3e 100%); }
  .photo--his-portrait { left: 364px; top: 74px; width: 147px; height: 97px; border-color: var(--border-orchid);
    background: linear-gradient(135deg, #4f7d2f 0%, #82a64d 40%, #b58d70 65%, #5b6fa0 100%); }
  .photo--park-bench { left: 34px; top: 247px; width: 147px; height: 219px; border-color: var(--border-violet);
    background: linear-gradient(180deg, #5c8f2e 0%, #8fbf4e 50%, #a98c64 78%, #7ea646 100%); }
  .photo--road-trip { left: 364px; top: 247px; width: 147px; height: 219px; border-color: var(--border-violet);
    background: linear-gradient(180deg, #87b74f 0%, #b6d58a 45%, #dcdcd2 70%, #6d8f45 100%); }
  .photo--first-kiss { left: 857px; top: 74px; width: 199px; height: 199px; border-color: var(--border-pink);
    background: radial-gradient(circle at 55% 40%, #f1f3dc 0%, #b4cf73 35%, #6e9a3a 70%, #506f2d 100%); }
  .photo--together { left: 579px; top: 296px; width: 231px; height: 170px; border-color: var(--border-orange);
    background: linear-gradient(120deg, #9cc04a 0%, #c9a48a 40%, #d98f8f 70%, #7aa23e 100%); }

  .ribbon {
    position: absolute; width: 145px; height: 21px;
    clip-path: polygon(0 0, 100% 0, 94% 50%, 100% 100%, 0 100%, 6% 50%);
    color: #fff; font-family: "Josefin Sans", sans-serif; font-weight: 300;
    font-size: 11px; letter-spacing: 1.6px; text-transform: uppercase;
    line-height: 23px; text-align: center;
  }
  .ribbon--how-we-met { left: 201px; top: 75px; background: var(--ribbon-green); }
  .ribbon--first-date { left: 201px; top: 448px; background: var(--ribbon-gold); }
  .ribbon--first-kiss { left: 689px; top: 75px; background: var(--ribbon-plum); }
  .ribbon--love-you { left: 841px; top: 448px; background: var(--ribbon-lavender); }

  .story {
    position: absolute; font-family: "Open Sans", sans-serif; font-size: 5.8px;
    line-height: 7.8px; color: var(--body-grey); text-align: justify;
  }
  .story p + p { margin-top: 7px; }
  .story--how-we-met { left: 202px; top: 110px; width: 140px; }
  .story--first-date { left: 202px; top: 323px; width: 140px; }
  .story--first-kiss { left: 579px; top: 110px; width: 250px; }
  .story--love-you { left: 841px; top: 353px; width: 213px; }
</style>
</head>
<body>
<main class="canvas">

  <section class="spread spread--cover" aria-label="Cover spread">
    <div class="cover-ribbon">to be continued...</div>
    <div class="spread__fold"></div>
    <div class="cover-frame">
      <svg width="432" height="437" viewBox="0 0 432 437" aria-hidden="true">
        <path d="M14,0 H418 A14,14 0 0 0 432,14 V423 A14,14 0 0 0 418,437 H14 A14,14 0 0 0 0,423 V14 A14,14 0 0 0 14,0 Z" fill="var(--frame-white)"/>
        <path d="M19,5 H413 A14,14 0 0 0 427,19 V418 A14,14 0 0 0 413,432 H19 A14,14 0 0 0 5,418 V19 A14,14 0 0 0 19,5 Z" fill="none" stroke="var(--frame-line)" stroke-width="1"/>
      </svg>
      <div class="cover-photo" role="img" aria-label="Cover photo of a smiling couple outdoors in summer greenery"></div>
      <h1 class="cover-title">moments with you...</h1>
    </div>
  </section>

  <section class="spread spread--inner" aria-label="Story spread">
    <div class="stripe-band stripe-band--top">
      <div class="stripe-band__line"></div><div class="stripe-band__line"></div><div class="stripe-band__line"></div><div class="stripe-band__line"></div><div class="stripe-band__line"></div>
      <div class="stripe-band__rule"></div>
    </div>
    <div class="stripe-band stripe-band--bottom">
      <div class="stripe-band__rule" style="margin-bottom:5px"></div>
      <div class="stripe-band__line"></div><div class="stripe-band__line"></div><div class="stripe-band__line"></div><div class="stripe-band__line"></div><div class="stripe-band__line"></div>
    </div>
    <div class="spread__fold"></div>

    <div class="photo photo--her-portrait" role="img" aria-label="Portrait photo of her in a sunny park"></div>
    <div class="ribbon ribbon--how-we-met">How we met</div>
    <div class="story story--how-we-met">
      <p>We met on a bright spring morning in the park, both reaching for the last bench in the shade. You laughed first, I laughed second, and we talked until the sun went down behind the trees.</p>
      <p>Neither of us planned to stay that long, yet neither of us wanted to leave. A coffee turned into dinner, and dinner turned into a story we still tell friends today.</p>
    </div>
    <div class="photo photo--his-portrait" role="img" aria-label="Portrait photo of him smiling outdoors"></div>

    <div class="photo photo--park-bench" role="img" aria-label="Photo of him sitting on a wooden bench under trees"></div>
    <div class="story story--first-date">
      <p>Our first date was a picnic with too many sandwiches and not enough napkins. We drove out of town with the windows down, singing loudly to songs we barely knew.</p>
      <p>The car broke down twice, the rain came early, and it was still the best day of the whole summer. We knew then this was something worth keeping.</p>
    </div>
    <div class="ribbon ribbon--first-date">Our first date</div>
    <div class="photo photo--road-trip" role="img" aria-label="Photo of a road trip in an open car among green trees"></div>

    <div class="ribbon ribbon--first-kiss">Our first kiss</div>
    <div class="story story--first-kiss">
      <p>It happened under the old oak tree at the end of a long walk, when the light turned gold and everything went quiet for a moment. Neither of us said a word, and that was perfect.</p>
      <p>We still walk past that tree every autumn, and every time we stop for a little while just to remember how it felt the very first time.</p>
    </div>
    <div class="photo photo--first-kiss" role="img" aria-label="Photo of the couple close together in soft sunlight"></div>

    <div class="photo photo--together" role="img" aria-label="Photo of the couple smiling together on a summer day"></div>
    <div class="story story--love-you">
      <p>You said it first, halfway through a silly joke, and then looked surprised at yourself. I said it right back before you could take it away, and we both started laughing.</p>
      <p>Three little words on an ordinary afternoon, and suddenly nothing about it felt ordinary at all. We have been saying them ever since, every single day.</p>
    </div>
    <div class="ribbon ribbon--love-you">First I love you</div>
  </section>

</main>
</body>
</html>
```